Letterhead for a German Distribution/Manufacturing Company

We need a professional Letterhead in a unique Design.
not to playful.
The Letterhead has to show show that we are a international company with headquater in Germany.
all details like adress, Vat Tax Number, Bank Accout, Eori, email, Company number has to be on the Letterhead.
for example use: VAT TAX DE5704168 Bank Account: Norrfeld Bank IBAN DE421705238ß310482 Swift: KOLV3154802 EORI 3041296587 Company Number: HRB 61508 Adress: VOLTRINA UG Amsel Strasse 7 Postal Code 04683 City Burgstädt Country: Germany Email: info@voltrina-example.com
the design can be colored but doesnt have to be
Industry/Entity Type
Manufacturing and international distribution
Requirements
Must have
- show that we are a international company with headquater in Germany. our company infos and logo

```html
<!DOCTYPE html>
<html lang="en">
<head>
<meta charset="utf-8">
<title>VOLTRINA Letterhead</title>
<link href="https://fonts.googleapis.com/css2?family=Montserrat:wght@400;500;600&family=Arimo:wght@400&display=swap" rel="stylesheet">
<style>
  :root {
    --brand-blue: #03487b;
    --rule-grey: #808080;
    --ink: #111;
    --ink-soft: #333;
    --paper: #fff;
    --backdrop: #f4f4f4;
  }
  * { margin: 0; padding: 0; box-sizing: border-box; }
  html, body { width: 1200px; height: 1200px; overflow: hidden; background: var(--backdrop); }
  .canvas { position: relative; width: 1200px; height: 1200px; }
  .sheet { position: absolute; left: 242.5px; top: 136px; width: 722.5px; height: 935px; background: var(--paper); }
  .abs { position: absolute; }
  .brand-block { left: 292.5px; top: 136px; width: 150px; height: 134.6px; background: var(--brand-blue);
    display: flex; align-items: center; justify-content: center; gap: 6px; }
  .brand-mark { width: 12px; height: 12px; border-radius: 50%; background: #fff; }
  .brand-name { font-family: "Montserrat", sans-serif; font-weight: 500; font-size: 16px; color: #fff; letter-spacing: 0.3px; }
  .header-rule { left: 442.5px; top: 237.5px; width: 522.5px; height: 10.5px; background: var(--rule-grey); }
  .head-text { font-family: "Montserrat", sans-serif; color: var(--ink); }
  .recipient { left: 293px; top: 288px; font-size: 14px; font-weight: 500; line-height: 1; }
  .recipient-role { left: 292px; top: 307px; font-size: 11px; font-weight: 500; }
  .date { right: 289px; top: 327px; font-size: 17.5px; font-weight: 500; }
  .company-ids { left: 294px; top: 358px; font-size: 14px; font-weight: 500; color: var(--ink-soft); line-height: 15.6px; letter-spacing: 0.3px; }
  .body-copy { left: 294px; width: 615px; font-family: "Arimo", Arial, sans-serif; font-size: 14.3px; line-height: 17.25px;
    color: var(--ink-soft); text-align: justify; }
  .para-one { top: 440px; }
  .para-two { top: 578px; text-align-last: left; }
  .spread-line { display: flex; justify-content: space-between; }
  .signatory { left: 292px; top: 819px; font-family: "Montserrat", sans-serif; font-size: 20px; font-weight: 500; color: var(--ink-soft); }
  .signature-area { left: 294px; top: 850px; width: 113.5px; height: 19px; background: #e6e6e6; }
  .footer-rule { top: 1007px; height: 9.5px; background: var(--rule-grey); }
  .footer-rule.left { left: 242.5px; width: 172px; }
  .footer-rule.right { left: 792.5px; width: 172.5px; }
  .footer-tab { left: 423px; top: 1007px; width: 361px; height: 20px; background: var(--brand-blue); }
  .footer-band { left: 242.5px; top: 1025px; width: 722.5px; height: 46px; background: var(--brand-blue); }
  .footer-country { left: 397px; top: 1036px; font-family: "Montserrat", sans-serif; font-size: 19.5px; font-weight: 500; color: #fff; letter-spacing: 0.8px; }
  .footer-divider { top: 1034px; width: 1.5px; height: 27px; background: #fff; }
  .footer-details { top: 1037px; font-family: "Montserrat", sans-serif; font-size: 8.2px; font-weight: 600; color: #fff; line-height: 10.5px; }
</style>
</head>
<body>
<div class="canvas">
  <div class="sheet"></div>

  <div class="abs brand-block">
    <span class="brand-mark"></span>
    <span class="brand-name">VOLTRINA</span>
  </div>
  <div class="abs header-rule"></div>

  <p class="abs head-text recipient">TO</p>
  <p class="abs head-text recipient-role">President / CEO</p>
  <p class="abs head-text date">1, april, 2023</p>

  <p class="abs head-text company-ids">VAT TAX DE5704168<br>Norrfeld Bank IBAN DE421705238ß310482</p>

  <div class="abs body-copy para-one">
    <p>"Lorem ipsum dolor sit amet, consectetur adipiscing elit, sed do eiusmod tempor incididunt ut labore et dolore magna aliqua. Ut enim ad minim veniam, quis nostrud exercitation ullamco laboris nisi ut aliquip ex ea commodo consequat. Duis aute irure dolor in reprehenderit in voluptate velit esse cillum dolore eu fugiat nulla pariatur. Excepteur sint occaecat cupidatat non proident, sunt in culpa qui officia deserunt mollit anim id est</p>
    <p class="spread-line"><span>l</span><span>a</span><span>b</span><span>o</span><span>r</span><span>u</span><span>m</span><span>.</span><span>"</span></p>
  </div>

  <p class="abs body-copy para-two">"Sed ut perspiciatis unde omnis iste natus error sit voluptatem accusantium doloremque laudantium, totam rem aperiam, eaque ipsa quae ab illo inventore veritatis et quasi architecto beatae vitae dicta sunt explicabo. Nemo enim ipsam voluptatem quia voluptas sit aspernatur aut odit aut fugit, sed quia consequuntur magni dolores eos qui ratione voluptatem sequi nesciunt. Neque porro quisquam est, qui dolorem ipsum quia dolor sit amet, consectetur, adipisci velit, sed quia non numquam eius modi tempora incidunt ut labore et dolore magnam aliquam quaerat voluptatem. Ut enim ad minima veniam, quis nostrum exercitationem ullam corporis suscipit laboriosam, nisi ut aliquid ex ea commodi consequatur? Quis autem vel eum iure reprehenderit qui in ea voluptate velit esse quam nihil molestiae consequatur, vel illum qui dolorem eum fugiat quo voluptas nulla pariatur?"</p>

  <p class="abs signatory">Director</p>
  <div class="abs signature-area" role="img" aria-label="Director's handwritten signature"></div>

  <div class="abs footer-rule left"></div>
  <div class="abs footer-rule right"></div>
  <div class="abs footer-tab"></div>
  <div class="abs footer-band"></div>
  <p class="abs footer-country">GERMANY</p>
  <div class="abs footer-divider" style="left:520px"></div>
  <p class="abs footer-details" style="left:537.5px">VOLTRINA UG Amsel Strasse 7 Postal<br>KOLV3154802 EORI 3041296587</p>
  <div class="abs footer-divider" style="left:710px"></div>
  <p class="abs footer-details" style="left:734px">HRB 61508<br>info@voltrina-example.com</p>
</div>
</body>
</html>
```